Home Page Design (+50 More Pages To Winning Designer!)

We have a 50+ page website, but we're starting with the home page. The winning designer will get all 50+ pages to design as a 2nd project, so make sure you do your best!

SoarVane is in the private jet industry and needs a re-designed website.

We have created the structure for the website and content inside of Tavoni.io (THESE ARE ONLY ROUGH A.I. GENERATED WIREFRAMES AND DO NOT NEED TO BE FOLLOWED EXACTLY) - https://www.tavoni.io/app/project/P482915_qRuVwKsLm-DDtaHrYuop72XNc8fkoPzqlrhwDxHkaWm3Tq

Take the content from the 'Home Page' under the 'Wireframe' tab on the Tavoni.io link above, but feel free to re-design the page in a better way as these are only A.I. generated wireframes.

We want a DARK theme.... High quality, luxurious feel, greyscale colors. Attached is a brand guideline (BUT THIS IS NOT A 100% BRAND GUIDELINE, YOU CAN CHANGE COLORS AND FONTS AND MAKE CHANGES IF YOU HAVE BETTER IDEAS) and attached is our logo. We are also attaching some examples of other apps and websites to give you a guideline of what we're looking for for this design project.

The final design MUST communicate luxury using high-quality imagery of large cabin luxurious private jets.

ENTRIES THAT DO NOT FOLLOW THE PROJECT BRIEF WILL BE AUTOMATICALLY DISCARDED. FOLLOW THE INSTRUCTIONS!

Industry/Entity Type

Travel

Number of Pages Required

1 page

Font styles to use
Sans Serif

Colors

Designer to choose colors to be used in the design.

Requirements
Must have
• Follow wireframe and use content in wireframe (see Tavoni.io link)

```html
<!DOCTYPE html>
<html lang="en">
<head>
<meta charset="utf-8">
<title>SoarVane — Luxury Private Jet Travel</title>
<link href="https://fonts.googleapis.com/css2?family=Exo+2:wght@300;400;500&family=Mulish:wght@400;600;700&display=swap" rel="stylesheet">
<style>
:root{
  --black:#0c0c0c;
  --ink:#161616;
  --char:#2b2b2b;
  --slate:#3a3a3a;
  --grey:#5a5a5a;
  --mist:#8a8a8a;
  --silver:#c9c9c9;
  --paper:#f2f2f2;
  --white:#ffffff;
  --gold:#f2c230;
  --line:rgba(255,255,255,.55);
  --head:'Exo 2',sans-serif;
  --body:'Mulish',sans-serif;
}
*{box-sizing:border-box;margin:0;padding:0}
html,body{width:1200px;height:4376px;overflow:hidden}
body{font-family:var(--body);color:var(--white);background:var(--black);position:relative}
section,header,footer{position:absolute;left:0;width:1200px;overflow:hidden}
.abs{position:absolute}
h1,h2,h3,h4{font-family:var(--head);font-weight:400}
.btn{display:inline-flex;align-items:center;justify-content:center;height:36px;padding:0 26px;font-size:11px;letter-spacing:.06em;text-transform:uppercase;font-family:var(--body);font-weight:600;border:1px solid var(--white);color:var(--white);background:transparent;min-width:118px}
.btn.solid{background:var(--white);color:var(--black)}
.btn.dark{background:var(--black);color:var(--white);border-color:var(--black)}
.btn.outline-dark{border-color:var(--black);color:var(--black)}
.btn-row{display:flex;gap:14px}
.eyebrow{font-size:9px;letter-spacing:.08em;text-transform:uppercase;display:flex;align-items:center;gap:8px}
.eyebrow::after{content:"";width:44px;height:1px;background:currentColor;opacity:.8}
.logo{font-family:var(--head);font-weight:300;font-size:28px;letter-spacing:.01em;display:flex;align-items:center;gap:6px}
.logo i{width:12px;height:12px;background:currentColor;display:inline-block}

/* header + hero */
.hero{top:0;height:560px;background:linear-gradient(90deg,#0b0b0b 0%,#141414 45%,#1e1d1b 100%)}
.hero-photo{right:0;top:0;width:560px;height:560px;background:radial-gradient(ellipse at 60% 70%,#8a6a3c 0%,#3b3128 30%,#161514 70%)}
.hero-photo::after{content:"";position:absolute;inset:0;background:linear-gradient(90deg,#141414 0%,rgba(20,20,20,0) 40%)}
.nav{top:14px;left:112px;width:976px;height:32px;display:flex;align-items:center}
.nav ul{display:flex;gap:24px;list-style:none;margin-left:38px;font-size:11.5px}
.nav li::after{content:" ⌄";font-size:10px}
.nav .btn{margin-left:auto;height:32px;min-width:116px;font-size:10px;padding:0 18px;gap:8px}
.hero h1{left:112px;top:250px;font-size:44px;line-height:1.2;width:560px}
.hero p{left:112px;top:366px;width:460px;font-size:11.5px;line-height:1.5;color:#e0e0e0}
.hero .btn-row{left:112px;top:434px}

/* search */
.search{top:560px;height:137px;background:var(--white);color:var(--black)}
.search .title{left:112px;top:32px;display:flex;align-items:center;gap:18px}
.search h2{font-size:18px}
.radio{display:flex;align-items:center;gap:6px;font-size:10px}
.radio span{width:9px;height:9px;border-radius:50%;border:1px solid #999}
.radio.on span{background:var(--black);border-color:var(--black)}
.search .row{left:112px;top:68px;display:flex;gap:13px}
.field{height:32px;border:1px solid #b8b8b8;font-size:10px;color:#888;display:flex;align-items:center;justify-content:space-between;padding:0 10px}
.field svg{width:14px;height:14px;stroke:#888;fill:none;stroke-width:1.2}
.search .go{height:32px;width:130px;background:var(--black);color:var(--white);font-size:11px;font-weight:600;display:flex;align-items:center;justify-content:center}

/* features */
.features{top:697px;height:228px;background:var(--black)}
.feature{top:54px;width:280px}
.feature .ico{width:60px;height:60px;border-radius:50%;border:1.5px solid var(--white);display:flex;align-items:center;justify-content:center;margin-bottom:18px}
.feature .ico svg{width:30px;height:30px;stroke:#fff;fill:none;stroke-width:1.5}
.feature h3{font-size:15px;margin-bottom:6px}
.feature p{font-size:10.5px;line-height:1.55;color:#d6d6d6}

/* fractional */
.fractional{top:925px;height:530px;background:linear-gradient(90deg,#6b6b6b,#4f4f4f 60%,#5d5d5d)}
.photo{background:linear-gradient(160deg,#8a8d93,#3c3e44)}
.frac-p1{left:112px;top:51px;width:296px;height:335px;background:linear-gradient(170deg,#c6b59a 0%,#5e5a56 45%,#2e2f33 100%)}
.frac-p2{left:286px;top:251px;width:241px;height:228px;border:2px solid #9a9a9a;background:linear-gradient(180deg,#d4d4d4,#7a7a7a 60%,#3b3b3b)}
.frac-copy{left:590px;top:132px;width:470px}
.frac-copy h2{font-size:30px;line-height:1.28;margin:12px 0 18px}
.frac-copy p{font-size:10.5px;line-height:1.55;color:#eee;width:440px}
.dots{display:flex;gap:14px;font-size:11px;margin:28px 0 30px}
.dots li{list-style:none;display:flex;align-items:center;gap:6px}
.dots li::before{content:"";width:11px;height:11px;border-radius:50%;background:#fff}

/* luxury */
.luxury{top:1455px;height:423px;background:linear-gradient(180deg,#272727,#333 60%,#2c2c2c)}
.lux-head{left:112px;top:62px}
.lux-head h2{font-size:30px;line-height:1.28;margin-top:12px}
.lux-side{left:610px;top:68px;width:480px}
.lux-side p{font-size:9.5px;line-height:1.55;color:#e4e4e4;margin-bottom:18px}
.card{top:197px;width:316px;height:164px;border:1px solid rgba(255,255,255,.7);padding:30px 26px}
.card svg{width:30px;height:30px;stroke:#fff;fill:none;stroke-width:1.4;margin-bottom:12px}
.card h3{font-size:15px;margin-bottom:6px}
.card p{font-size:10px;line-height:1.55;color:#aaa}

/* cta light */
.cta-light{top:1878px;height:238px;background:linear-gradient(180deg,#ffffff 40%,#dcdfe3 100%);color:var(--black);text-align:center}
.cta-light h2{margin-top:58px;font-size:30px}
.cta-light p{font-size:10.5px;margin:12px 0 16px}
.cta-light .btn-row{justify-content:center}

/* experience */
.experience{top:2116px;height:538px;background:linear-gradient(90deg,#3b3b3b,#575757 70%,#676767)}
.exp-photo{left:835px;top:0;width:365px;height:538px;background:linear-gradient(180deg,#9da3ad,#d8dbe0 50%,#8e939c)}
.exp-jet{left:440px;top:150px;width:560px;height:330px;background:radial-gradient(ellipse at 60% 45%,rgba(230,232,236,.9) 0%,rgba(160,165,175,.6) 30%,rgba(90,90,90,0) 65%)}
.exp-copy{left:112px;top:112px;width:480px}
.exp-copy h2{font-size:30px;line-height:1.28;margin:12px 0 18px}
.exp-copy p{font-size:10.5px;line-height:1.5;color:#eee;width:440px}
.exp-cols{display:flex;gap:40px;margin:26px 0 30px}
.exp-cols div{width:215px}
.exp-cols h4{font-size:14px;display:flex;align-items:center;gap:6px;margin-bottom:6px}
.exp-cols h4::before{content:"";width:11px;height:11px;border-radius:50%;background:#fff}
.exp-cols p{font-size:10px;padding-left:17px;width:auto}

/* faq */
.faq{top:2654px;height:727px;background:linear-gradient(180deg,#262626,#303030 70%,#3a3a3a)}
.faq-photo{left:112px;top:95px;width:408px;height:534px;border:2px solid #8a8a8a;background:linear-gradient(170deg,#a08a70 0%,#7c7b7e 40%,#5a6478 75%,#c9b597 100%)}
.faq-copy{left:604px;top:112px;width:484px}
.faq-copy h2{font-size:30px}
.faq-copy .lead{font-size:10px;margin:10px 0 18px;color:#ddd}
.qa{border:1px solid rgba(255,255,255,.85);height:42px;display:flex;align-items:center;justify-content:space-between;padding:0 16px;font-size:12.5px;margin-bottom:12px}
.qa b{font-weight:400;font-size:16px}
.qa.open{height:109px;flex-direction:column;align-items:flex-start;justify-content:flex-start;padding:12px 16px;background:var(--white);color:var(--black)}
.qa.open p{font-size:10px;line-height:1.45;margin-top:10px}
.faq-copy h4{font-size:13px;margin-top:20px}
.faq-copy .small{font-size:9.5px;color:#bbb;margin:4px 0 18px}

/* testimonial */
.testimonial{top:3381px;height:456px;background:linear-gradient(180deg,#f6f6f6,#e8e9ea 60%,#cfd1d3);color:var(--black)}
.quote{left:112px;top:94px;width:500px;font-size:29px;line-height:1.3}
.stars{left:112px;top:270px;display:flex;gap:8px}
.stars svg{width:14px;height:14px;fill:var(--gold)}
.author{left:112px;top:304px;display:flex;align-items:center;gap:28px}
.author h4{font-size:18px}
.author small{font-size:9px}
.author .sep{width:1px;height:52px;background:#888}
.author .brand{font-family:var(--head);font-size:15px;font-weight:500;display:flex;align-items:center;gap:6px}
.author .brand i{width:10px;height:10px;background:var(--black);display:inline-block}
.test-photo{left:673px;top:51px;width:415px;height:330px;background:linear-gradient(120deg,#2c2c2e 0%,#6a6d72 35%,#bdbfc3 60%,#4b4d52 100%)}
.arrows{left:748px;top:345px;width:130px;height:58px;background:#333;display:flex}
.arrows span{flex:1;display:flex;align-items:center;justify-content:center}
.arrows span+span{border-left:1px solid #777}
.arrows svg{width:26px;height:12px;stroke:#fff;fill:none;stroke-width:1.3}

/* cta dark */
.cta-dark{top:3837px;height:260px;background:linear-gradient(180deg,#2d2d2d,#1a1a1a 50%,#2a2a2a);text-align:center}
.cta-dark h2{margin-top:52px;font-size:30px}
.cta-dark p{font-size:10px;line-height:1.5;width:690px;margin:12px auto 18px;color:#eee}
.cta-dark .btn-row{justify-content:center}

/* footer */
.footer{top:4097px;height:279px;background:var(--black)}
.footer .logo{left:112px;top:62px}
.follow{left:112px;top:130px;font-size:10px}
.socials{display:flex;gap:9px;margin-top:8px}
.socials span{width:22px;height:22px;border-radius:50%;border:1px solid #fff}
.fcol{top:42px}
.fcol h4{font-size:15px;margin-bottom:10px}
.fcol li{list-style:none;font-size:8.5px;color:#ccc;margin-bottom:9px}
.news{left:770px;top:42px;width:318px}
.news h4{font-size:15px;margin-bottom:8px}
.news .sm{font-size:8.5px;color:#bbb}
.news form{display:flex;gap:8px;margin:14px 0 10px}
.news .in{flex:1;height:32px;border:1px solid #fff;font-size:9px;display:flex;align-items:center;padding:0 12px}
.news .sub{width:98px;height:32px;background:#fff;color:#000;font-size:10px;font-weight:600;display:flex;align-items:center;justify-content:center}
.legal{left:112px;top:226px;width:976px;border-top:1px solid #444;padding-top:14px;display:flex;justify-content:center;gap:22px;font-size:8.5px;color:#ccc}
</style>
</head>
<body>

<header class="hero">
  <div class="abs hero-photo" role="img" aria-label="Private jet on a runway at sunset, seen from the front"></div>
  <nav class="abs nav">
    <div class="logo">SoarVane</div>
    <ul>
      <li>Aircraft</li><li>Programs</li><li>Why SoarVane</li><li>Lifestyle</li><li>Sustainability</li><li>Resources</li><li>Competitors</li>
    </ul>
    <a class="btn">Inquire
      <svg width="11" height="11" viewBox="0 0 12 12" fill="#fff"><path d="M1 6 11 1 8 11 6 7z"/></svg>
    </a>
  </nav>
  <h1 class="abs">Experience the Ultimate in Luxury Jet Travel</h1>
  <p class="abs">SoarVane offers fractional jet ownership, jet card programs, private jet lease programs, all access programs, helicopter access programs, and by the seat charter flights. Discover the perfect flight program for your needs.</p>
  <div class="abs btn-row"><a class="btn solid">Explore</a><a class="btn">Learn More</a></div>
</header>

<section class="search">
  <div class="abs title">
    <h2>Search Your Flight</h2>
    <div class="radio on"><span></span>Round Trip</div>
    <div class="radio"><span></span>One Way</div>
  </div>
  <div class="abs row">
    <div class="field" style="width:163px">Departure Airport<svg viewBox="0 0 16 16"><path d="M8 1v14M2 8h12M5 12h6"/></svg></div>
    <div class="field" style="width:163px">Arrival Airport<svg viewBox="0 0 16 16"><path d="M8 1v14M2 8h12M5 12h6"/></svg></div>
    <div class="field" style="width:163px">Departure Date<svg viewBox="0 0 16 16"><rect x="2" y="3" width="12" height="11"/><path d="M2 6h12M5 1v3M11 1v3"/></svg></div>
    <div class="field" style="width:163px">Return Date<svg viewBox="0 0 16 16"><rect x="2" y="3" width="12" height="11"/><path d="M2 6h12M5 1v3M11 1v3"/></svg></div>
    <div class="field" style="width:90px">Pax<svg viewBox="0 0 16 16"><path d="M4 6l4 4 4-4"/></svg></div>
    <div class="go">Search</div>
  </div>
</section>

<section class="features">
  <div class="abs feature" style="left:112px">
    <div class="ico"><svg viewBox="0 0 30 30"><path d="M4 20c4-2 7-2 10 0l6-2c2 0 2 2 0 3l-8 3-8-1"/><circle cx="16" cy="10" r="5"/></svg></div>
    <h3>Flexible Ownership Options Available</h3>
    <p>Choose from a variety of ownership programs and enjoy the freedom to fly on your own terms.</p>
  </div>
  <div class="abs feature" style="left:469px">
    <div class="ico"><svg viewBox="0 0 30 30"><circle cx="13" cy="9" r="4"/><path d="M5 22c0-5 4-7 8-7"/><rect x="15" y="16" width="11" height="8" rx="1"/><path d="M15 19h11"/></svg></div>
    <h3>Convenient Jet Card Programs</h3>
    <p>Access a fleet of private jets with our exclusive jet card programs, offering flexibility and conve-</p>
  </div>
  <div class="abs feature" style="left:826px">
    <div class="ico"><svg viewBox="0 0 30 30"><path d="M6 24l6-6M10 14l6 6 8-8-6-6z"/><circle cx="8" cy="8" r="2"/><path d="M20 3l1 2 2 1-2 1-1 2-1-2-2-1 2-1z"/></svg></div>
    <h3>Flexible Lease Programs</h3>
    <p>Experience the luxury of private jet travel without the commitment with our flexible lease programs.</p>
  </div>
</section>

<section class="fractional">
  <div class="abs frac-p1" role="img" aria-label="Businessman in a suit standing beside a private jet"></div>
  <div class="abs frac-p2" role="img" aria-label="Black and white front view of a private jet on the tarmac"></div>
  <div class="abs frac-copy">
    <div class="eyebrow">Discover</div>
    <h2>Experience the Luxury of<br>Fractional Jet Ownership</h2>
    <p>With SoarVane's fractional jet ownership program, you can enjoy the benefits of private jet travel without the hassle and expense of owning a whole aircraft. Our program offers flexibility, convenience, and access to a fleet of luxurious jets, allowing you to travel in style and comfort.</p>
    <ul class="dots"><li>Flexible Ownership Options</li><li>Convenient Booking Process</li><li>Luxurious Fleet of Jets</li></ul>
    <div class="btn-row"><a class="btn solid">Learn More</a><a class="btn">Sign Up</a></div>
  </div>
</section>

<section class="luxury">
  <div class="abs lux-head">
    <div class="eyebrow">Luxury</div>
    <h2>Experience the Ultimate in<br>Private Jet Travel</h2>
  </div>
  <div class="abs lux-side">
    <p>SoarVane offers a wide range of exclusive services to meet your private jet travel needs. From fractional jet ownership to on-demand charter flights, we provide the highest level of luxury and convenience.</p>
    <div class="btn-row"><a class="btn solid">Learn More</a><a class="btn">Sign Up</a></div>
  </div>
  <div class="abs card" style="left:112px">
    <svg viewBox="0 0 30 30"><circle cx="15" cy="11" r="7"/><circle cx="15" cy="11" r="3"/><path d="M11 17l-2 10 6-3 6 3-2-10"/></svg>
    <h3>On-Demand Charter</h3>
    <p>Fly anywhere, anytime with our on-demand charter service.</p>
  </div>
  <div class="abs card" style="left:442px">
    <svg viewBox="0 0 30 30"><circle cx="15" cy="15" r="11"/><path d="M4 15h22M15 4c-5 6-5 16 0 22M15 4c5 6 5 16 0 22M6 9h18M6 21h18"/></svg>
    <h3>Global Medical Response &amp; Recovery</h3>
    <p>We provide specialized medical transportation services worldwide.</p>
  </div>
  <div class="abs card" style="left:772px">
    <svg viewBox="0 0 30 30"><circle cx="20" cy="9" r="5"/><path d="M16 13L5 24l3 3M9 20l3 3"/></svg>
    <h3>Fractional Jet Ownership</h3>
    <p>Enjoy the benefits of owning a private jet without the hassles.</p>
  </div>
</section>

<section class="cta-light">
  <h2>Experience luxury travel like never before</h2>
  <p>Contact us today to book your exclusive jet experience</p>
  <div class="btn-row"><a class="btn dark">Learn More</a><a class="btn outline-dark">Sign Up</a></div>
</section>

<section class="experience">
  <div class="abs exp-photo" role="img" aria-label="Sky with soft white clouds"></div>
  <div class="abs exp-jet" role="img" aria-label="Private jet flying above the clouds"></div>
  <div class="abs exp-copy">
    <div class="eyebrow">Experience</div>
    <h2>Unparalleled Luxury and<br>Convenience for Private Aviation</h2>
    <p>Discover the ultimate in luxury and convenience with SoarVane. Our exclusive private aviation solutions provide you with unparalleled access to the world of private jets, ensuring a seamless and extraordinary travel experience.</p>
    <div class="exp-cols">
      <div><h4>Convenience</h4><p>Enjoy hassle-free travel with our flexible scheduling and personalized services.</p></div>
      <div><h4>Luxury</h4><p>Indulge in the lavish amenities and exquisite interiors of our private jets.</p></div>
    </div>
    <div class="btn-row"><a class="btn solid">Learn More</a><a class="btn">Sign Up</a></div>
  </div>
</section>

<section class="faq">
  <div class="abs faq-photo" role="img" aria-label="Woman on a phone call seated in a private jet cabin"></div>
  <div class="abs faq-copy">
    <h2>Frequently</h2>
    <p class="lead">Find answers to common questions about SoarVane's services and programs.</p>
    <div class="qa">What is SoarVane?<b>+</b></div>
    <div class="qa open">How it works?<p>SoarVane works by allowing customers to purchase fractional ownership of a private jet, join jet card programs for a set number of flight hours, lease a private jet for a specific period, or access our all access and helicopter programs. We also offer charter flights where customers can book individual seats on private jets.</p></div>
    <div class="qa">Why choose SoarVane?<b>+</b></div>
    <div class="qa">How to book?<b>+</b></div>
    <div class="qa">What are the benefits?<b>+</b></div>
    <h4>Still have questions?</h4>
    <p class="small">Contact us for more information.</p>
    <div class="btn-row"><a class="btn solid">Learn More</a><a class="btn">Sign Up</a></div>
  </div>
</section>

<section class="testimonial">
  <p class="abs quote">SoarVane's services have exceeded my expectations. The convenience and luxury of flying with them is unmatched.</p>
  <div class="abs stars">
    <svg viewBox="0 0 20 20"><path d="M10 1l2.6 6 6.4.5-4.9 4.2 1.5 6.3L10 14.7 4.4 18l1.5-6.3L1 7.5 7.4 7z"/></svg>
    <svg viewBox="0 0 20 20"><path d="M10 1l2.6 6 6.4.5-4.9 4.2 1.5 6.3L10 14.7 4.4 18l1.5-6.3L1 7.5 7.4 7z"/></svg>
    <svg viewBox="0 0 20 20"><path d="M10 1l2.6 6 6.4.5-4.9 4.2 1.5 6.3L10 14.7 4.4 18l1.5-6.3L1 7.5 7.4 7z"/></svg>
    <svg viewBox="0 0 20 20"><path d="M10 1l2.6 6 6.4.5-4.9 4.2 1.5 6.3L10 14.7 4.4 18l1.5-6.3L1 7.5 7.4 7z"/></svg>
    <svg viewBox="0 0 20 20"><path d="M10 1l2.6 6 6.4.5-4.9 4.2 1.5 6.3L10 14.7 4.4 18l1.5-6.3L1 7.5 7.4 7z"/></svg>
  </div>
  <div class="abs author">
    <div><h4>John Doe</h4><small>CEO, Acme Corp</small></div>
    <div class="sep"></div>
    <div class="brand"><i></i>Lumenfold</div>
  </div>
  <div class="abs test-photo" role="img" aria-label="Man in a grey suit and sunglasses walking beside a jet engine"></div>
  <div class="abs arrows">
    <span><svg viewBox="0 0 26 12"><path d="M25 6H2M7 1L2 6l5 5"/></svg></span>
    <span><svg viewBox="0 0 26 12"><path d="M1 6h23M19 1l5 5-5 5"/></svg></span>
  </div>
</section>

<section class="cta-dark">
  <h2>Experience luxury travel like never before</h2>
  <p>Discover the ultimate in private jet travel with SoarVane. Whether you're looking for fractional jet ownership, jet card programs, private jet lease programs, all access programs, helicopter access programs, or by the seat charter flights, we have the perfect solution for your travel needs.</p>
  <div class="btn-row"><a class="btn solid">Book</a><a class="btn">Contact</a></div>
</section>

<footer class="footer">
  <div class="abs logo">SoarVane</div>
  <div class="abs follow">FOLLOW US:
    <div class="socials"><span></span><span></span><span></span><span></span></div>
  </div>
  <div class="abs fcol" style="left:357px"><h4>About Us</h4><ul><li>Charter</li><li>Fleet</li><li>Destinations</li><li>Pricing</li><li>Contact</li></ul></div>
  <div class="abs fcol" style="left:500px"><h4>Services</h4><ul><li>Private Jets</li><li>Helicopters</li><li>Jet Cards</li><li>Membership</li><li>FAQ</li></ul></div>
  <div class="abs fcol" style="left:643px"><h4>Terms</h4><ul><li>TERMS</li><li>Privacy</li><li>Careers</li><li>Press</li><li>Blog</li><li>Support</li></ul></div>
  <div class="abs news">
    <h4>Subscribe to Our Newsletter</h4>
    <p class="sm">Join our mailing list for the latest updates.</p>
    <form><div class="in">Enter Your Email</div><div class="sub">SUBSCRIBE</div></form>
    <p class="sm">By subscribing, you agree to our Privacy Policy and consent<br>to receive updates</p>
  </div>
  <div class="abs legal"><span>© 2024 SoarVane. All rights reserved.</span><span>Privacy Policy</span><span>Terms of Service</span><span>Cookie Settings</span></div>
</footer>

</body>
</html>
```